Soho based IT support firm flyer.

We need a flyer to boost our business. We're a tech support firm based in Soho, London and provide helpdesk and call out support to SMEs in and around London.
They'll be two flyers with the same design. One is location specific and has the copy:
-
1 Month Free IT Support!
Based in Soho, we provide expert tech support for both desktops and laptops.
We have monthly as well as pay-as-you-go plans to fit your business.
Call us now and we'll show you how we can save you up to 50% on your IT spend.
-None location based is-
1 Month Free IT Support!
We provide expert, professional tech support for both desktops and laptops.
• Dedicated full time helpdesk
• Same day onsite visits
• Proactive support with monitoring
• 98% satisfaction score*
*taken from satisfaction survey sent out on closure of every case for Oct 2011 to Oct 2012
-
The location one needs to include a map with our location marked as postcode W9K 4TP.
I'm fine with royalty photos being used within a reasonable price. Please use PixQuarry.
Our site shows our brand best. Please keep as close to this as possible.
http://brisk-byte.example
Thanks for looking.

```html
<!DOCTYPE html>
<html lang="en">
<head>
<meta charset="utf-8">
<title>BriskByte – 1 Month Free I.T. Support</title>
<link rel="stylesheet" href="https://fonts.googleapis.com/css2?family=Arimo:ital,wght@0,400;0,700;1,400;1,700&display=swap">
<style>
  :root {
    --brand-green: #9ac21b;
    --ribbon-green: #c4dc36;
    --ribbon-fold: #8ea51c;
    --band-green: #c8de4a;
    --page-tint: #f4f7ea;
    --top-strip: #e2e3d6;
    --text-grey: #474747;
    --orange: #f7a131;
    --footer-grey: #484848;
    --white: #ffffff;
  }
  * { margin: 0; padding: 0; box-sizing: border-box; }
  html, body { width: 851px; height: 1200px; overflow: hidden; }
  body { font-family: "Arimo", Arial, sans-serif; background: var(--page-tint); }
  .flyer { position: relative; width: 851px; height: 1200px; overflow: hidden; background: var(--page-tint); }

  .top-strip { position: absolute; left: 0; top: 0; width: 100%; height: 10px; background: var(--top-strip); }
  .header { position: absolute; left: 0; top: 10px; width: 100%; height: 93px; background: #f8f9f2;
    display: flex; align-items: center; justify-content: center; }
  .brand-name { font-size: 50px; font-weight: 700; color: var(--brand-green); letter-spacing: -0.5px; }

  .hero { position: absolute; left: 0; top: 103px; width: 100%; height: 317px;
    background: linear-gradient(90deg, #2f5a12 0%, #7fae2c 12%, #3d6a14 24%, #a8cf46 38%, #4f7f18 50%, #9cc63a 63%, #365f10 76%, #86b52e 88%, #2c5510 100%); }
  .hero-band { position: absolute; left: 0; top: 420px; width: 100%; height: 10px; background: var(--band-green); }

  .tagline { position: absolute; left: 175px; top: 143px; width: 483px; height: 158px;
    background: rgba(40, 55, 20, 0.55); border-radius: 4px; text-align: center; color: var(--white);
    text-shadow: 0 1px 2px rgba(0,0,0,.5); }
  .tagline-kicker { margin-top: 12px; font-size: 13px; font-weight: 700; }
  .tagline-title { font-size: 37px; font-weight: 700; line-height: 38px; }
  .tagline-sub { font-size: 35px; line-height: 38px; }
  .tagline-text { margin-top: 8px; font-size: 11px; line-height: 18px; }

  .card { position: absolute; left: 131px; top: 338px; width: 574px; height: 712px; background: var(--white);
    box-shadow: 0 0 3px rgba(0,0,0,.15); }

  .ribbon { position: absolute; left: 101px; top: 388px; width: 575px; height: 90px; background: var(--ribbon-green);
    display: flex; align-items: center; justify-content: center; color: var(--white); font-size: 36px;
    padding-top: 6px; text-shadow: 0 1px 2px rgba(0,0,0,.35); box-shadow: 0 2px 2px rgba(0,0,0,.15); }
  .ribbon strong { font-weight: 700; margin-right: 9px; }
  .ribbon-fold { position: absolute; left: 101px; top: 478px; }

  .offer-copy { position: absolute; left: 165px; top: 516px; width: 515px; color: var(--text-grey);
    font-size: 22px; line-height: 31px; }
  .offer-copy p + p { margin-top: 32px; }

  .location { position: absolute; left: 134px; top: 800px; width: 568px; height: 247px; background: var(--orange); }
  .map { position: absolute; left: 20px; top: 18px; width: 322px; height: 212px;
    background: linear-gradient(135deg, #ecebe4 0%, #e3e1d8 45%, #f2d38a 50%, #e6e4dc 55%, #dfe6d4 100%); }
  .address { position: absolute; left: 352px; top: 76px; width: 206px; text-align: center; color: var(--white); }
  .address-label { font-size: 14px; font-style: italic; }
  .address-lines { font-size: 19px; font-weight: 700; line-height: 20px; }

  .footer { position: absolute; left: 0; top: 1050px; width: 100%; height: 150px; background: var(--footer-grey);
    text-align: center; color: var(--white); }
  .footer-brand { margin-top: 18px; font-size: 34px; font-weight: 700; color: var(--white); }
  .footer-rule { width: 440px; height: 1px; margin: 14px auto 0; background: rgba(255,255,255,.2); }
  .footer-lead { margin-top: 5px; font-size: 18px; font-style: italic; }
  .contact-list { margin-top: 8px; list-style: none; display: flex; justify-content: center; font-size: 18px; }
  .contact-list li + li::before { content: "\25CF"; font-size: 12px; margin: 0 16px; vertical-align: 2px; }
</style>
</head>
<body>
<div class="flyer">
  <div class="top-strip"></div>
  <header class="header"><span class="brand-name">BriskByte</span></header>

  <div class="hero" role="img" aria-label="Blurred close-up photograph of green grass blades"></div>
  <div class="hero-band"></div>

  <div class="tagline">
    <p class="tagline-kicker">WE'RE ABOUT</p>
    <h1 class="tagline-title">Friendly &amp; Reliable</h1>
    <p class="tagline-sub">Tech Support</p>
    <p class="tagline-text">IT Support, Consultancy and Project Management. A one stop shop<br>for all of your business' IT needs.</p>
  </div>

  <div class="card"></div>

  <div class="ribbon"><strong>1 Month Free</strong> I.T. Support!</div>
  <svg class="ribbon-fold" width="30" height="30" viewBox="0 0 30 30" aria-hidden="true">
    <polygon points="0,0 30,0 30,30" fill="var(--ribbon-fold)"/>
  </svg>

  <div class="offer-copy">
    <p>Based in Soho,We provide expert, professional tech support for both desktops and laptops.</p>
    <p>We have monthly as well as pay-as-you-go plans to fit your business.</p>
    <p>Call us now and we'll show you how we can save you up to 50% on your IT spend.</p>
  </div>

  <section class="location">
    <div class="map" role="img" aria-label="Street map of the office area with a red pin marking the office location"></div>
    <div class="address">
      <p class="address-label">Visit us at:</p>
      <p class="address-lines">12-14 Marlow House,<br>Harcourt Street,<br>London<br>W9K 4TP</p>
    </div>
  </section>

  <footer class="footer">
    <p class="footer-brand">BriskByte</p>
    <div class="footer-rule"></div>
    <p class="footer-lead">You can also contact us at:</p>
    <ul class="contact-list">
      <li>Ph.: 0203 555 0147</li>
      <li>Email: info@brisk-byte.example</li>
      <li>Website: www.brisk-byte.example</li>
    </ul>
  </footer>
</div>
</body>
</html>
```